Brenmoor Group needs a business card

I would like the card to be simple but modern and elegant.
I like black and white.
or black and gold.
we are a private finance lender and also are involved in property and property developments.

please look at the business card photos i provided i would like B.G only one one side and all the other details on the other side use fonts that tie in with my theme.

Industry/Entity Type

Finance

Contact Information for Business Card

Brenmoor Group (B.G) Callum Brenmoor M: 0418396152 E: callumbren@quivomail.com

Font styles to use
Other font styles liked:
• Use fonts that would reflect our business

Colors
000000
ffffff

Requirements
Must have
• one side of details
• other side has either B.G or Brenmoor Group like in the photos provided

```html
<!DOCTYPE html>
<html lang="en">
<head>
<meta charset="utf-8">
<title>Brenmoor Group — Business Card</title>
<link rel="stylesheet" href="https://fonts.googleapis.com/css2?family=Jost:wght@500&family=PT+Sans:wght@700&family=Arimo:wght@400&display=swap">
<style>
  :root {
    --ink: #000000;
    --paper: #ffffff;
    --backdrop: #ececec;
  }
  * { margin: 0; padding: 0; box-sizing: border-box; }
  html, body {
    width: 1200px;
    height: 1200px;
    overflow: hidden;
    background: var(--backdrop);
  }
  .canvas {
    position: relative;
    width: 1200px;
    height: 1200px;
  }
  .card {
    position: absolute;
    left: 240px;
    width: 720px;
    height: 440px;
  }
  .card--front {
    top: 127px;
    background: var(--ink);
    color: var(--paper);
  }
  .card--back {
    top: 633px;
    background: var(--paper);
    color: var(--ink);
  }

  /* Company name: one font, one weight, one colour, one plain square */
  .company {
    position: absolute;
    display: flex;
    align-items: center;
    font-family: "Jost", "Century Gothic", sans-serif;
    font-weight: 500;
    line-height: 1;
    white-space: nowrap;
  }
  .company__mark {
    flex: none;
    background: currentColor;
  }
  .card--front .company {
    left: 0;
    right: 0;
    top: 190px;
    justify-content: center;
    font-size: 54px;
    gap: 18px;
  }
  .card--front .company__mark { width: 16px; height: 16px; }

  .card--back .company {
    right: 46px;
    top: 80px;
    font-size: 30px;
    gap: 10px;
  }
  .card--back .company__mark { width: 10px; height: 10px; }

  .holder {
    position: absolute;
    right: 46px;
    top: 148px;
    font-family: "PT Sans", "Myriad Pro", sans-serif;
    font-weight: 700;
    font-size: 38px;
    line-height: 1;
    white-space: nowrap;
  }
  .holder__rule {
    position: absolute;
    right: 46px;
    top: 196px;
    width: 79px;
    height: 3px;
    background: var(--ink);
  }

  .contact {
    position: absolute;
    left: 47px;
    top: 330px;
    list-style: none;
    font-family: "Arimo", Arial, sans-serif;
    font-size: 27px;
    line-height: 40px;
    white-space: nowrap;
  }
  .contact__label { display: inline-block; width: 42px; }
  .contact__item--email .contact__label { padding-left: 3px; }
</style>
</head>
<body>
<main class="canvas">
  <section class="card card--front" aria-label="Business card front">
    <div class="company">
      <span class="company__mark" aria-hidden="true"></span>
      <span class="company__name">Brenmoor Group</span>
    </div>
  </section>

  <section class="card card--back" aria-label="Business card back">
    <div class="company">
      <span class="company__mark" aria-hidden="true"></span>
      <span class="company__name">Brenmoor Group</span>
    </div>
    <h1 class="holder">Callum Brenmoor</h1>
    <div class="holder__rule"></div>
    <ul class="contact">
      <li class="contact__item contact__item--mobile"><span class="contact__label">M:</span>0418396152</li>
      <li class="contact__item contact__item--email"><span class="contact__label">E:</span>callumbren@quivomail.com</li>
    </ul>
  </section>
</main>
</body>
</html>
```